Poster of Insipirational Quotes

Attached is a list of leadership quotes from Arlen Drubeck. I would like a poster made, incorporating whatever design elements you like, potentially including Arlen's face, and one or more of the quotes. I intend to print this out in A3 or larger to hang on my wall.

The quotes are:

Being responsible sometimes means pissing people off.

The day soldiers stop bringing you their problems is the day you have stopped leading them.

Don't be buffaloed by experts and elites. Experts often possess more data than judgment. Elites can become so inbred that they produce hemophiliacs who bleed to death as soon as they are nicked by the real world.

Don't be afraid to challenge the pros, even in their own backyard.

Never neglect details. When everyone's mind is dulled or distracted the leader must be doubly vigilant.

You don't know what you can get away with until you try.

Keep looking below surface appearances. Don't shrink from doing so (just) because you might not like what you find.

Organization doesn't really accomplish anything. Plans don't accomplish anything, either. Theories of management don't much matter. Endeavors succeed or fail because of the people involved. Only by attracting the best people will you accomplish great deeds.

Organization charts and fancy titles count for next to nothing.

Never let your ego get so close to your position that when your position goes, your ego goes with it.

Fit no stereotypes. Don't chase the latest management fads. The situation dictates which approach best accomplishes the team's mission.

Perpetual optimism is a force multiplier.

Look for intelligence and judgment, and most critically, a capacity to anticipate, to see around corners. Also look for loyalty, integrity, a high energy drive, a balanced ego, and the drive to get things done.

Great leaders are almost always great simplifiers, who can cut through argument, debate and doubt, to offer a solution everybody can understand.

The commander in the field is always right and the rear echelon is wrong, unless proved otherwise.

Have fun in your command. Don't always run at a breakneck pace. Take leave when you've earned it: Spend time with your families. Corollary: surround yourself with people who take their work seriously, but not themselves, those who work hard and play hard.

Command is lonely.

Leadership is the art of accomplishing more than the science of management
says is possible.
Updates

I need to modify the specification based on the designs that I've seen.

Target Market(s)

Executive Office

Colors

Designer to choose colors to be used in the design.

Requirements
Must have
• Quotes

```html
<!DOCTYPE html>
<html lang="en">
<head>
<meta charset="utf-8">
<title>Leadership Quote Poster</title>
<link rel="stylesheet" href="https://fonts.googleapis.com/css2?family=Marcellus&display=swap">
<style>
  :root {
    --backdrop: #eceeef;
    --paper: #ffffff;
    --ink: #111111;
    --portrait-tone: #c9c9c9;
    --portrait-fade: #ffffff;
  }
  * { margin: 0; padding: 0; box-sizing: border-box; }
  html, body {
    width: 1200px;
    height: 923px;
    overflow: hidden;
    background: var(--backdrop);
  }
  .canvas {
    position: relative;
    width: 1200px;
    height: 923px;
  }
  .poster {
    position: absolute;
    left: 328px;
    top: 78px;
    width: 545px;
    height: 766px;
    background: var(--paper);
    overflow: hidden;
  }
  .portrait-area {
    position: absolute;
    left: 40px;
    top: 30px;
    width: 465px;
    height: 720px;
    background:
      radial-gradient(ellipse 38% 22% at 50% 22%, rgba(170,170,170,0.55), rgba(255,255,255,0) 100%),
      radial-gradient(ellipse 55% 45% at 50% 62%, rgba(190,190,190,0.45), rgba(255,255,255,0) 100%);
  }
  .quote {
    position: absolute;
    left: 0;
    top: 108px;
    width: 100%;
    text-align: center;
    font-family: "Marcellus", serif;
    font-size: 62px;
    line-height: 81px;
    color: var(--ink);
    text-transform: uppercase;
    letter-spacing: 0;
  }
  .quote span { display: block; }
</style>
</head>
<body>
  <div class="canvas">
    <div class="poster">
      <div class="portrait-area" role="img" aria-label="Faded portrait of a man in glasses, suit and tie, gesturing with both hands"></div>
      <blockquote class="quote">
        <span>"Being</span>
        <span>Responsible</span>
        <span>Sometimes</span>
        <span>Means</span>
        <span>Pissing</span>
        <span>People</span>
        <span>Off."</span>
      </blockquote>
    </div>
  </div>
</body>
</html>
```